"Maple Hollow" red wine label design

We are a Sydney based company. We need to design a wine label for a Australian red wine.
Front label include following info:
Our brand: "Maple Hollow";
Product name: "Shiraz 2016";
In the bottom with small font: "Wine of Australia", "750ml"
Back label:
the back label would need to be consistent with the front label, with space for one paragraph of tasting notes, and ingredient info etc.
we would like to use white, gold and blue in this label. It should make customer feel the magical and beautiful moment of starry night.

We also need a logo design for the wine brand: "Maple Hollow"

I have attached a few wine bottle that used blue to give you some inspirations.

We need the design in AI file format.

Target Market(s)

both men and women

Industry/Entity Type

It Company

Logo Text

Maple Hollow

Requirements
Nice to have
• gold borderline, words; use of blue and white

```html
<!DOCTYPE html>
<html lang="en">
<head>
<meta charset="utf-8">
<title>Maple Hollow – Shiraz 2016 Label</title>
<link rel="stylesheet" href="https://fonts.googleapis.com/css2?family=Cinzel:wght@400;500&display=swap">
<style>
  :root {
    --page-bg: #e4e8e8;
    --night-deep: #05070f;
    --night-navy: #0d1640;
    --night-blue: #1d2f8a;
    --night-glow: #2a46c4;
    --label-text: #f4f5fa;
  }
  * { margin: 0; padding: 0; box-sizing: border-box; }
  html, body {
    width: 1200px;
    height: 1200px;
    overflow: hidden;
    background: var(--page-bg);
  }
  .canvas {
    position: relative;
    width: 1200px;
    height: 1200px;
    display: flex;
    align-items: center;
    justify-content: center;
  }
  .wine-label {
    position: relative;
    width: 900px;
    height: 868px;
    overflow: hidden;
    font-family: "Cinzel", "Trajan Pro", serif;
    color: var(--label-text);
    text-align: center;
  }
  .night-sky {
    position: absolute;
    inset: 0;
    background:
      radial-gradient(ellipse 55% 45% at 85% 12%, var(--night-glow) 0%, rgba(42,70,196,0) 70%),
      radial-gradient(ellipse 70% 50% at 30% 35%, rgba(29,47,138,0.7) 0%, rgba(29,47,138,0) 75%),
      linear-gradient(180deg, var(--night-navy) 0%, var(--night-blue) 38%, #0b1336 56%, var(--night-deep) 68%, var(--night-deep) 100%);
  }
  .brand-name {
    position: absolute;
    top: 165px;
    left: 0;
    right: 0;
    font-size: 74px;
    font-weight: 500;
    letter-spacing: 2px;
    line-height: 1;
  }
  .wine-variety {
    position: absolute;
    top: 298px;
    left: 0;
    right: 0;
    font-size: 44px;
    font-weight: 400;
    letter-spacing: 1px;
    line-height: 1;
  }
  .origin {
    position: absolute;
    top: 706px;
    left: 0;
    right: 0;
    font-size: 36px;
    font-weight: 400;
    line-height: 1;
  }
  .volume {
    position: absolute;
    top: 786px;
    left: 0;
    right: 0;
    font-size: 26px;
    font-weight: 400;
    line-height: 1;
  }
</style>
</head>
<body>
  <main class="canvas">
    <section class="wine-label">
      <div class="night-sky" role="img" aria-label="Photograph of a starry night sky over a dark silhouetted treeline"></div>
      <h1 class="brand-name">Maple Hollow</h1>
      <p class="wine-variety">Shiraz 2016</p>
      <p class="origin">Wine of Australia</p>
      <p class="volume">750 ML</p>
    </section>
  </main>
</body>
</html>
```